Security Consulting firm needs an ad design

We need a 3.375” x 4.875” ad design for our core services. The ad should include the company logo and the content from the first half of the attached sample JPG (Without the sentence under the title but including the description for the Plan - Design - Deploy - Manage and the titles ) as well as the following corporate information:
www.corvanthpartners.us
82 Marbury Ave. Suite 615, Alderbrook, NJ 07412
PHONE 888-416-2057 / EMAIL info@corvanthpartners.us
The design should incorporate the same blue color that is in our logo and the font Raleway. Also - please use the same icons that are in the sample JPG - they can also be extracted from the attached indesign file.
The ad is to be publish in print and digital issue.
Please provide with all source files as well as a hi-res PDF using press quality or similar PDF settings.
- Raleway

```html
<!DOCTYPE html>
<html lang="en">
<head>
<meta charset="utf-8">
<title>Corvanth Partners – Creating Secure Environments</title>
<link href="https://fonts.googleapis.com/css2?family=Raleway:wght@400;500;700;800;900&display=swap" rel="stylesheet">
<style>
  :root {
    --navy: #131c2c;
    --navy-mid: #1f2c40;
    --brand-blue: #2f76b8;
    --bright-blue: #41a3e8;
    --panel: #e9f1f9;
    --divider: #cdd6e0;
    --text-gray: #555b63;
    --white: #ffffff;
  }
  * { margin: 0; padding: 0; box-sizing: border-box; }
  html, body { width: 831px; height: 1200px; overflow: hidden; background: var(--white); }
  body { font-family: "Raleway", sans-serif; }
  .ad { position: relative; width: 831px; height: 1200px; overflow: hidden; background: var(--navy); }

  .hero-photo {
    position: absolute; left: 400px; top: 0; width: 431px; height: 540px;
    background: linear-gradient(90deg, var(--navy) 0%, #3a4556 35%, #7c8594 70%, #a6acb6 100%);
  }
  .brand { position: absolute; left: 52px; top: 62px; display: flex; align-items: center; gap: 12px; }
  .brand-mark { width: 20px; height: 20px; border-radius: 50%; background: var(--bright-blue); }
  .brand-name { color: var(--white); font-weight: 800; font-size: 40px; letter-spacing: -0.5px; line-height: 1; }

  .headline { position: absolute; left: 50px; top: 172px; }
  .headline span { display: block; line-height: 1; }
  .headline .lead { color: var(--white); font-weight: 400; font-size: 59px; letter-spacing: -1px; }
  .headline .big { color: var(--bright-blue); font-weight: 900; font-size: 106px; letter-spacing: -2px; margin-top: 2px; }
  .headline .sub { color: var(--bright-blue); font-weight: 800; font-size: 57px; letter-spacing: -0.5px; margin-top: 2px; }

  .services { position: absolute; left: 0; top: 540px; width: 831px; height: 463px; background: var(--panel); }
  .col-divider { position: absolute; left: 416px; width: 3px; background: var(--divider); }
  .service { position: absolute; width: 380px; text-align: center; }
  .service-badge {
    position: absolute; width: 140px; height: 140px; border-radius: 50%; background: var(--panel);
    display: flex; align-items: center; justify-content: center;
  }
  .service-badge .disc {
    width: 114px; height: 114px; border-radius: 50%; background: var(--white);
    box-shadow: 2px 3px 6px rgba(0,0,0,0.18);
    display: flex; align-items: center; justify-content: center;
  }
  .service-title { color: var(--brand-blue); font-weight: 800; font-size: 31px; line-height: 1; }
  .service-text { color: var(--text-gray); font-weight: 500; font-size: 21.5px; line-height: 26px; margin-top: 10px; }

  .rule { position: absolute; left: 0; top: 1003px; width: 831px; height: 13px; background: var(--navy-mid); }
  .contact { position: absolute; left: 0; top: 1016px; width: 831px; height: 184px; background: var(--brand-blue); color: var(--white); }
  .contact-divider { position: absolute; left: 417px; top: 25px; width: 2px; height: 78px; background: rgba(255,255,255,0.18); }
  .phone { position: absolute; left: 86px; top: 30px; display: flex; align-items: center; gap: 10px; font-weight: 800; font-size: 35px; line-height: 1; }
  .email { position: absolute; left: 86px; top: 70px; display: flex; align-items: center; gap: 10px; font-weight: 400; font-size: 23px; line-height: 1; }
  .address { position: absolute; left: 447px; top: 34px; display: flex; gap: 10px; font-weight: 400; font-size: 23px; line-height: 30px; }
  .website { position: absolute; left: 0; top: 120px; width: 831px; text-align: center; font-weight: 700; font-size: 33px; letter-spacing: 3px; }
</style>
</head>
<body>
<div class="ad">
  <div class="hero-photo" role="img" aria-label="Photo of a security operator wearing a headset in a dimly lit monitoring room"></div>

  <div class="brand">
    <span class="brand-mark"></span>
    <span class="brand-name">Corvanth Partners</span>
  </div>

  <h1 class="headline">
    <span class="lead">CREATING</span>
    <span class="big">SECURE</span>
    <span class="sub">ENVIRONMENTS</span>
  </h1>

  <section class="services">
    <div class="col-divider" style="top:32px;height:160px"></div>
    <div class="col-divider" style="top:282px;height:160px"></div>

    <div class="service-badge" style="left:157px;top:-70px"><div class="disc">
      <svg width="56" height="66" viewBox="0 0 56 66" fill="none" stroke="#2f76b8" stroke-width="4" stroke-linecap="round" stroke-linejoin="round">
        <rect x="4" y="9" width="48" height="54" rx="4"/><rect x="18" y="3" width="20" height="11" rx="3" fill="#2f76b8"/>
        <path d="M12 26l4 4 6-7M12 39l4 4 6-7M12 52l4 4 6-7"/><path d="M28 28h16M28 41h16M28 54h16"/>
      </svg></div></div>
    <div class="service" style="left:37px;top:77px">
      <div class="service-title">PLAN</div>
      <div class="service-text">Security Assessment and<br>Planning Services</div>
    </div>

    <div class="service-badge" style="left:538px;top:-70px"><div class="disc">
      <svg width="80" height="80" viewBox="0 0 80 80">
        <g fill="#2f76b8">
          <path d="M33 4h12l2 9 7 3 8-5 8 8-5 8 3 7 9 2v12l-9 2-3 7 5 8-8 8-8-5-7 3-2 9H33l-2-9-7-3-8 5-8-8 5-8-3-7-9-2V34l9-2 3-7-5-8 8-8 8 5 7-3z"/>
        </g>
        <circle cx="39" cy="40" r="17" fill="#fff"/>
        <path d="M30 26a10 10 0 0 0 11 14l26 26a5 5 0 0 0 7-7L48 33a10 10 0 0 0-14-11l7 7-3 5-5 1z" fill="#2f76b8" stroke="#fff" stroke-width="3"/>
      </svg></div></div>
    <div class="service" style="left:418px;top:77px">
      <div class="service-title">DESIGN</div>
      <div class="service-text">Security Design and<br>Engineering</div>
    </div>

    <div class="service-badge" style="left:155px;top:184px"><div class="disc">
      <svg width="64" height="64" viewBox="0 0 64 64" fill="#2f76b8">
        <path d="M60 4c-14 0-26 6-34 18l-9 1-9 9 11 2 11 11 2 11 9-9 1-9c12-8 18-20 18-34z"/>
        <circle cx="44" cy="20" r="5" fill="#fff"/>
        <path d="M14 42c-5 2-8 8-8 16 8 0 14-3 16-8z" fill="none" stroke="#2f76b8" stroke-width="4"/>
      </svg></div></div>
    <div class="service" style="left:35px;top:331px">
      <div class="service-title">DEPLOY</div>
      <div class="service-text">Procurement and Project<br>Management Services</div>
    </div>

    <div class="service-badge" style="left:535px;top:190px"><div class="disc">
      <svg width="80" height="72" viewBox="0 0 80 72" fill="#2f76b8">
        <circle cx="40" cy="11" r="9"/>
        <path d="M24 38c0-10 7-16 16-16s16 6 16 16z"/>
        <ellipse cx="40" cy="40" rx="20" ry="7"/>
        <path d="M40 46v16M22 44L8 50M58 44l14 6" stroke="#2f76b8" stroke-width="4"/>
        <circle cx="40" cy="64" r="6"/><circle cx="7" cy="51" r="6"/><circle cx="73" cy="51" r="6"/>
      </svg></div></div>
    <div class="service" style="left:415px;top:335px">
      <div class="service-title">MANAGE</div>
      <div class="service-text">Comprehensive Security<br>Program Management</div>
    </div>
  </section>

  <div class="rule"></div>

  <footer class="contact">
    <div class="contact-divider"></div>
    <div class="phone">
      <svg width="26" height="26" viewBox="0 0 24 24" fill="#fff"><path d="M6.6 10.8a15 15 0 0 0 6.6 6.6l2.2-2.2c.3-.3.7-.4 1-.2 1.1.4 2.300.6 3.6.6.6 0 1 .4 1 1V20c0 .6-.4 1-1 1A17 17 0 0 1 3 4c0-.6.4-1 1-1h3.5c.6 0 1 .4 1 1 0 1.3.2 2.5.6 3.6.1.3 0 .7-.2 1z"/></svg>
      <span>888-416-2057</span>
    </div>
    <div class="email">
      <svg width="28" height="20" viewBox="0 0 28 20" fill="#fff"><path d="M0 0h28v20H0z"/><path d="M1 1l13 10L27 1" fill="none" stroke="#2f76b8" stroke-width="2.5"/></svg>
      <span>info@corvanthpartners.us</span>
    </div>
    <div class="address">
      <svg width="20" height="28" viewBox="0 0 20 28" style="margin-top:2px"><path d="M10 0a10 10 0 0 0-10 10c0 7 10 18 10 18s10-11 10-18A10 10 0 0 0 10 0z" fill="#fff"/><circle cx="10" cy="10" r="4" fill="#2f76b8"/></svg>
      <span>82 Marbury Ave. Suite 615,<br>Alderbrook, NJ 07412</span>
    </div>
    <div class="website">www.corvanthpartners.us</div>
  </footer>
</div>
</body>
</html>
```